Copper & Wren Labels*

Hello :) I am needing labels for my herbal tea/petal product. I am a small producer for the local restaurants (edible flowers/micro herbs & dried product). I am hoping to sell the dried product online. It will be sold in batches as it is ready so quite small/boutique and the label needs to be somewhat generic for the range of produce I make.
Feels: no/minimal plastic, product is in a reusable mason jar, we use organic/regenerative principles from soil health to end product. Treading gently on the land. High quality i.e only fresh hand picked leaf tips for the tea.

```html
<!DOCTYPE html>
<html lang="en">
<head>
<meta charset="utf-8">
<title>Copper &amp; Wren — label concepts</title>
<link rel="stylesheet" href="https://fonts.googleapis.com/css2?family=Lobster+Two&family=Nunito:wght@400;600;700;800&display=swap">
<style>
  :root {
    --page: #ffffff;
    --ink: #1f2a1f;
    --ink-soft: #3a3a3a;
    --sage: #d6e4c4;
    --sage-bright: #a3cf8c;
    --forest: #2f6d49;
    --cream: #f5f3ee;
    --paper-white: #ecebea;
    --paper-grey: #dcdad7;
    --rule: #3b3b3b;
    --shadow: #c9c8c6;
  }
  * { box-sizing: border-box; margin: 0; padding: 0; }
  html, body { width: 1200px; height: 848px; overflow: hidden; background: var(--page); }
  body { position: relative; font-family: "Nunito", sans-serif; color: var(--ink); }

  .row-number {
    position: absolute; left: 100px; width: 30px;
    font: 800 38px/1 "Nunito", sans-serif; color: var(--ink);
  }

  .label { position: absolute; overflow: hidden; }
  .label--front-wide { left: 175px; width: 366px; }
  .label--front-narrow { left: 581px; width: 243px; }
  .label--info { left: 865px; width: 200px; }
  .row-1 .label { top: 81px; height: 201px; }
  .row-2 .label { top: 325px; height: 199px; }
  .row-3 .label { top: 566px; height: 199px; }

  .paper--cream { background: var(--cream); }
  .paper--white { background: linear-gradient(180deg, #f1f0ef, var(--paper-white)); box-shadow: 0 0 0 4px var(--shadow); }
  .paper--grey { background: linear-gradient(180deg, #e3e1de, var(--paper-grey)); box-shadow: 0 0 0 4px var(--shadow); }

  .framed::after {
    content: ""; position: absolute; inset: 4px; border: 1px solid var(--rule); pointer-events: none;
  }

  .botanical-art {
    position: absolute; top: 0; bottom: 0;
    background: linear-gradient(135deg, #e7e6e0, #cfcec7 55%, #e9e8e2);
  }
  .botanical-art--left { left: 0; width: 81px; }
  .botanical-art--right { right: 0; width: 81px; }
  .label--front-narrow .botanical-art--left { width: 17px; }
  .label--front-narrow .botanical-art--right { width: 41px; }

  .band {
    position: absolute; top: 0; bottom: 0;
    display: flex; flex-direction: column; align-items: center;
    padding-top: 10px; text-align: center;
  }
  .band--sage { background: var(--sage); }
  .band--bright { background: var(--sage-bright); }
  .label--front-wide .band { left: 81px; width: 204px; }
  .label--front-narrow .band { left: 17px; width: 185px; }
  .row-2 .band, .row-3 .band { top: 4px; bottom: 4px; }

  .brand-mark { display: flex; flex-direction: column; align-items: center; }
  .brand-mark__dot { width: 46px; height: 46px; border-radius: 50%; background: var(--ink); }
  .row-1 .brand-mark__dot { background: var(--forest); }
  .row-3 .brand-mark__dot { width: 54px; height: 54px; }
  .brand-mark__name { font: 800 15px/1.3 "Nunito", sans-serif; color: var(--ink); }
  .row-1 .brand-mark__name { color: var(--forest); }

  .product-title {
    margin-top: 8px;
    font: 400 30px/1 "Lobster Two", cursive; color: var(--ink); white-space: nowrap;
  }
  .row-2 .product-title { color: var(--forest); }
  .label--front-narrow .product-title { font-size: 27px; }

  .tagline { margin-top: 10px; font: 600 10.5px/1.2 "Nunito", sans-serif; letter-spacing: .3px; color: var(--ink-soft); }
  .tagline__sub { font: 600 8.5px/1.3 "Nunito", sans-serif; color: var(--ink-soft); }
  .label--front-narrow .tagline { font-size: 9.8px; }
  .label--front-narrow .tagline__sub { font-size: 8px; }

  .info-table {
    position: absolute; inset: 6px;
    display: grid; grid-template-columns: 1fr 1fr;
    grid-template-rows: 44px 30px 60px 1fr;
    border: 1px solid var(--rule);
    font-family: "Nunito", sans-serif; color: var(--ink-soft); text-align: center;
  }
  .info-table > * { border-bottom: 1px solid var(--rule); }
  .info-cell--full { grid-column: 1 / 3; }
  .info-heading { font: 700 11px/1.25 "Nunito", sans-serif; padding-top: 8px; text-transform: uppercase; }
  .info-leaf { font-size: 8px; font-weight: 700; padding-top: 4px; text-transform: uppercase; }
  .info-leaf span { display: block; text-transform: none; font-weight: 600; font-size: 7.5px; }
  .info-field { font-size: 8px; font-weight: 700; padding-top: 5px; text-transform: uppercase; }
  .info-field + .info-field { border-left: 1px solid var(--rule); }
  .info-origin {
    grid-column: 1 / 3; border-bottom: none;
    display: flex; align-items: center; justify-content: space-between; padding: 0 8px;
    text-align: left; font-size: 8px; font-weight: 700; line-height: 1.3; text-transform: uppercase;
  }
  .origin-badge { width: 40px; height: 40px; border-radius: 50%; background: var(--ink); }
</style>
</head>
<body>

<section class="row-1">
  <div class="row-number" style="top:112px">1</div>

  <div class="label label--front-wide paper--cream">
    <div class="botanical-art botanical-art--left" role="img" aria-label="Line drawing of leaves and flower buds"></div>
    <div class="botanical-art botanical-art--right" role="img" aria-label="Line drawing of leaves and flower buds"></div>
    <div class="band band--sage">
      <div class="brand-mark"><span class="brand-mark__dot"></span><span class="brand-mark__name">hollowbrook</span></div>
      <div class="product-title">Copper &amp; Wren</div>
      <p class="tagline">GROWN, HARVESTED AND DRIED</p>
      <p class="tagline__sub">Chemical free on our farm in east Kelsmere</p>
    </div>
  </div>

  <div class="label label--front-narrow paper--cream">
    <div class="botanical-art botanical-art--left" role="img" aria-label="Line drawing of leaves"></div>
    <div class="botanical-art botanical-art--right" role="img" aria-label="Line drawing of leaves"></div>
    <div class="band band--sage">
      <div class="brand-mark"><span class="brand-mark__dot"></span><span class="brand-mark__name">hollowbrook</span></div>
      <div class="product-title">Copper &amp; Wren</div>
      <p class="tagline">GROWN, HARVESTED AND DRIED</p>
      <p class="tagline__sub">Chemical free on our farm in east Kelsmere</p>
    </div>
  </div>

  <div class="label label--info paper--cream">
    <div class="info-table">
      <div class="info-cell--full info-heading">Single origin<br>herbal tea etc.</div>
      <div class="info-cell--full info-leaf">Leaf base<span>Lemon Verbena, Mint, Agastache</span></div>
      <div class="info-field">Petals</div>
      <div class="info-field">Batch</div>
      <div class="info-origin"><span>Tallow Creek<br>Victoria Australia</span><span class="origin-badge"></span></div>
    </div>
  </div>
</section>

<section class="row-2">
  <div class="row-number" style="top:410px">2</div>

  <div class="label label--front-wide paper--white framed">
    <div class="band band--sage">
      <div class="brand-mark"><span class="brand-mark__dot"></span><span class="brand-mark__name">hollowbrook</span></div>
      <div class="product-title">Copper &amp; Wren</div>
      <p class="tagline">GROWN, HARVESTED AND DRIED</p>
      <p class="tagline__sub">Chemical free on our farm in east Kelsmere</p>
    </div>
  </div>

  <div class="label label--front-narrow paper--white framed">
    <div class="band band--sage">
      <div class="brand-mark"><span class="brand-mark__dot"></span><span class="brand-mark__name">hollowbrook</span></div>
      <div class="product-title">Copper &amp; Wren</div>
      <p class="tagline">GROWN, HARVESTED AND DRIED</p>
      <p class="tagline__sub">Chemical free on our farm in east Kelsmere</p>
    </div>
  </div>

  <div class="label label--info paper--white">
    <div class="info-table">
      <div class="info-cell--full info-heading">Single origin<br>herbal tea etc.</div>
      <div class="info-cell--full info-leaf">Leaf base<span>Lemon Verbena, Mint, Agastache</span></div>
      <div class="info-field">Petals</div>
      <div class="info-field">Batch</div>
      <div class="info-origin"><span>Tallow Creek<br>Victoria Australia</span><span class="origin-badge"></span></div>
    </div>
  </div>
</section>

<section class="row-3">
  <div class="row-number" style="top:655px">3</div>

  <div class="label label--front-wide paper--grey framed">
    <div class="band band--bright">
      <div class="brand-mark"><span class="brand-mark__dot"></span><span class="brand-mark__name">hollowbrook</span></div>
      <div class="product-title">Copper &amp; Wren</div>
      <p class="tagline">GROWN, HARVESTED AND DRIED</p>
      <p class="tagline__sub">Chemical free on our farm in east Kelsmere</p>
    </div>
  </div>

  <div class="label label--front-narrow paper--grey framed">
    <div class="band band--bright">
      <div class="brand-mark"><span class="brand-mark__dot"></span><span class="brand-mark__name">hollowbrook</span></div>
      <div class="product-title">Copper &amp; Wren</div>
      <p class="tagline">GROWN, HARVESTED AND DRIED</p>
      <p class="tagline__sub">Chemical free on our farm in east Kelsmere</p>
    </div>
  </div>

  <div class="label label--info paper--grey">
    <div class="info-table">
      <div class="info-cell--full info-heading">Single origin<br>herbal tea etc.</div>
      <div class="info-cell--full info-leaf">Leaf base<span>Lemon Verbena, Mint, Agastache</span></div>
      <div class="info-field">Petals</div>
      <div class="info-field">Batch</div>
      <div class="info-origin"><span>Tallow Creek<br>Victoria Australia</span><span class="origin-badge"></span></div>
    </div>
  </div>
</section>

</body>
</html>
```